Hops, Riffs & Sunset Grillout.

I need an A3 Poster, Insta Square and Facebook Event Cover photo for a Hops Riffs and Grill Event. Details as follows:

Name: Hops, Riffs and Sunset Grill
12pm - Late. Jan 26th at Copperleaf Yard Brewhouse
Acts:
Blue Tern - 7pm
Velvet Kite & Slow Morris - 3pm - 7pm
Grant Whitcombe - 12pm -3pm

Free BBQ 2-4pm.

```html
<!DOCTYPE html>
<html lang="en">
<head>
<meta charset="utf-8">
<title>Hops, Riffs and Sunset Grill</title>
<link rel="stylesheet" href="https://fonts.googleapis.com/css2?family=Alfa+Slab+One&display=swap">
<style>
  :root {
    --page: #ffffff;
    --ember-dark: #3a1a12;
    --ember-mid: #8a3418;
    --ember-warm: #c8601f;
    --ale-gold: #d99a22;
    --ale-amber: #a8521a;
    --band: rgba(70, 24, 18, 0.82);
    --band-soft: rgba(70, 24, 18, 0.72);
    --logo-panel: rgba(58, 22, 18, 0.85);
    --ink: #ffffff;
    --ink-soft: #efe6e2;
  }
  * { box-sizing: border-box; margin: 0; padding: 0; }
  html, body {
    width: 899px; height: 1200px; overflow: hidden;
    background: var(--page);
  }
  .canvas {
    position: relative; width: 899px; height: 1200px;
    background: var(--page);
  }
  .poster {
    position: absolute; left: 116px; top: 131px;
    width: 662px; height: 944px; overflow: hidden;
    font-family: "Alfa Slab One", Georgia, serif;
    color: var(--ink);
    text-align: center;
  }
  .poster-photo {
    position: absolute; inset: 0;
    background:
      radial-gradient(ellipse 42% 60% at 74% 60%, var(--ale-gold) 0%, var(--ale-amber) 45%, transparent 75%),
      radial-gradient(ellipse 50% 40% at 18% 30%, var(--ember-warm) 0%, transparent 70%),
      radial-gradient(ellipse 50% 30% at 25% 92%, var(--ember-warm) 0%, transparent 70%),
      linear-gradient(160deg, var(--ember-mid) 0%, var(--ember-dark) 55%, var(--ember-mid) 100%);
  }
  .band {
    position: absolute; left: 0; width: 100%;
    background: var(--band);
    display: flex; flex-direction: column; justify-content: center; align-items: center;
    clip-path: polygon(0 0, 100% 0, 94% 50%, 100% 100%, 0 100%, 6% 50%);
  }
  .band--title {
    top: 0; height: 160px;
    font-size: 46px; line-height: 1.15; letter-spacing: 0.5px;
    clip-path: polygon(0 0, 100% 0, 94% 50%, 100% 100%, 0 100%, 6% 50%);
  }
  .band--date { top: 408px; height: 85px; font-size: 27px; line-height: 1.2; background: var(--band-soft); }
  .band--act { font-size: 28px; line-height: 1.3; }
  .band--headliner { top: 513px; height: 56px; }
  .band--afternoon { top: 585px; height: 92px; }
  .band--opener { top: 685px; height: 84px; background: var(--band-soft); }
  .band--freebbq { top: 848px; height: 84px; font-size: 38px; }
  .act-time { color: var(--ink-soft); }
  .venue-mark {
    position: absolute; left: 137px; top: 161px; width: 391px; height: 225px;
    background: var(--logo-panel);
    display: flex; flex-direction: column; justify-content: center; align-items: center;
    color: var(--ink); line-height: 1.05;
  }
  .venue-mark__main { font-size: 50px; }
  .venue-mark__sub { font-size: 40px; }
  .venue-mark__tail { font-size: 22px; letter-spacing: 6px; margin-top: 8px; }
</style>
</head>
<body>
<div class="canvas">
  <section class="poster">
    <div class="poster-photo" role="img" aria-label="Sizzling barbecue meat on a grill beside a tall glass of amber beer, with drifting smoke"></div>

    <h1 class="band band--title"><span>HOPS, RIFFS AND</span><span>SUNSET GRILL</span></h1>

    <div class="venue-mark">
      <span class="venue-mark__main">COPPERLEAF</span>
      <span class="venue-mark__sub">YARD</span>
      <span class="venue-mark__tail">BREWHOUSE</span>
    </div>

    <p class="band band--date"><span>12pm - Late. Jan 26th at</span><span>COPPERLEAF YARD BREWHOUSE</span></p>

    <p class="band band--act band--headliner"><span>BLUE TERN - 7pm</span></p>
    <p class="band band--act band--afternoon"><span>VELVET KITE &amp; SLOW MORRIS</span><span class="act-time">3pm - 7pm</span></p>
    <p class="band band--act band--opener"><span>GRANT WHITCOMBE</span><span class="act-time">12pm - 3pm</span></p>

    <p class="band band--freebbq"><span>FREE BBQ 2-4pm.</span></p>
  </section>
</div>
</body>
</html>
```